Create banner ads for a digital product that deletes personal information from the web

The context of the banners is general advertisement for our service.
Please provide us with a set of static and flash/gif banners in the following standard sizes for the theme you create:
160x600
300x250
300x600
320x250
336x280
728x90
Please see our website for logo (just our name) and theme ideas - please follow similar color/font schemes if possible. www.quietlanternhub.com
Our company is an online service that deletes personal information from the internet for our members (automated opt-outs and content removal). Our target audience is anyone who wishes to protect their personal information from being on the internet (i.e. prefer to fly under the internet radar, for example). This is a product for U.S. residents who value privacy and online reputation. We seek to provide members with control of what 300+ websites are sharing about them – removing names, addresses, ages, phone numbers, email addresses, children’s information, home/property value information etc.
Industry/Entity Type
Internet
Look and feel
Each slider illustrates characteristics of the customer's brand and the style your logo design should communicate.

```html
<!DOCTYPE html>
<html lang="en">
<head>
<meta charset="utf-8">
<title>QuietLanternHub – Privacy Banner 300x600</title>
<link rel="stylesheet" href="https://fonts.googleapis.com/css2?family=Open+Sans:wght@300;400;600;700;800&display=swap">
<style>
  :root {
    --sky-top: #2f78bd;
    --sky-mid: #8db9dc;
    --sky-glow: #fbf6e4;
    --field-light: #b7d25a;
    --field-mid: #7fa930;
    --field-dark: #4d7a18;
    --white: #ffffff;
    --ink: #111111;
    --ink-soft: #1e2a33;
    --button-top: #6fd06a;
    --button-bottom: #2f9a36;
    --button-edge: #27802c;
  }
  html, body {
    margin: 0;
    padding: 0;
    width: 1200px;
    height: 2400px;
    overflow: hidden;
    background: #ffffff;
  }
  .banner {
    position: relative;
    width: 1200px;
    height: 2400px;
    overflow: hidden;
    font-family: "Open Sans", Arial, sans-serif;
  }
  .scene-backdrop {
    position: absolute;
    inset: 0;
    background:
      radial-gradient(ellipse 620px 520px at 640px 1540px, rgba(255,252,235,0.95) 0%, rgba(255,248,220,0.55) 45%, rgba(255,248,220,0) 100%),
      radial-gradient(ellipse 500px 700px at 1150px 300px, rgba(245,205,150,0.55) 0%, rgba(245,205,150,0) 100%),
      linear-gradient(180deg,
        var(--sky-top) 0%,
        #4f90cb 22%,
        var(--sky-mid) 45%,
        var(--sky-glow) 62%,
        var(--field-light) 68%,
        var(--field-mid) 82%,
        var(--field-dark) 100%);
  }
  .headline {
    position: absolute;
    left: 0;
    width: 1200px;
    top: 56px;
    margin: 0;
    text-align: center;
    padding-left: 80px;
    box-sizing: border-box;
    color: var(--white);
    font-weight: 700;
    font-size: 150px;
    line-height: 158px;
    letter-spacing: -2px;
    text-shadow: 0 3px 10px rgba(0,40,90,0.35);
  }
  .headline-rest {
    position: absolute;
    left: 400px;
    top: 540px;
    margin: 0;
    color: var(--white);
    font-weight: 300;
    font-size: 112px;
    line-height: 112px;
    text-shadow: 0 3px 10px rgba(0,40,90,0.3);
  }
  .threats {
    position: absolute;
    left: 520px;
    width: 680px;
    top: 770px;
    margin: 0;
    text-align: center;
    color: var(--ink-soft);
    font-weight: 400;
    font-size: 64px;
    line-height: 78px;
  }
  .scan-offer {
    position: absolute;
    left: 40px;
    width: 400px;
    top: 1090px;
    margin: 0;
    text-align: center;
    color: var(--ink);
    font-weight: 700;
    font-size: 52px;
    line-height: 72px;
    letter-spacing: -1px;
  }
  .cta-button {
    position: absolute;
    left: 296px;
    top: 1996px;
    width: 604px;
    height: 196px;
    border-radius: 98px;
    background: linear-gradient(180deg, var(--button-top) 0%, #4cb84c 50%, var(--button-bottom) 100%);
    border: 4px solid var(--button-edge);
    box-sizing: border-box;
    box-shadow: 0 8px 16px rgba(0,0,0,0.25);
    display: flex;
    align-items: center;
    justify-content: center;
    color: var(--white);
    font-weight: 600;
    font-size: 66px;
    text-decoration: none;
    text-shadow: 0 2px 4px rgba(0,0,0,0.3);
  }
  .brand-name {
    position: absolute;
    left: 0;
    width: 1200px;
    top: 2226px;
    margin: 0;
    text-align: center;
    color: var(--white);
    font-weight: 600;
    font-size: 116px;
    line-height: 140px;
    letter-spacing: -2px;
  }
</style>
</head>
<body>
  <div class="banner">
    <div class="scene-backdrop" role="img" aria-label="Photo of a man with raised arms standing in a green field under a bright, sunlit blue sky with clouds"></div>

    <h1 class="headline">Your<br>Personal<br>Privacy</h1>
    <p class="headline-rest">is threatened<br>daily</p>

    <p class="threats">by identity thieves,<br>marketers, scammers<br>and creepers.</p>

    <p class="scan-offer">See what<br>others can<br>find out<br>about you<br>online<br>with a<br>free scan</p>

    <a class="cta-button" href="#">Get Started Now!</a>

    <p class="brand-name">QuietLanternHub</p>
  </div>
</body>
</html>
```